RK Teardown business cards v.2 first was me

So the ones in the picture are my original cards that I came up with. 😅however I kinda messed up on two things, I missed spelled my name it should be Marcello Vantosa as well as the email should be Marcellov@brightlanecrews.com. I would like to clean this card up and also make it pop! Something that people would remember me by and that screams DEMOLITION. As well as a card that give you a feeling of loyalty and trust. I would also like to change and remove junk hauling and add full demolition to replace it. These cards worked for a little while but I cant make that my image while handing these out. I would also like to only put down that we are located in Cedar Ridge, CA, 92511 instead of the address on the card. Also if we can have a line that states Licensed, Bonded, & Insured. With out License # 4837215

Target Market(s)

Contractors and Home owners

Industry/Entity Type

Construction specialist in Demolition

Contact Information for Business Card

R Teardown Selective Demolition & Full Demolition Kitchens AD Preparation Bathrooms Sheds Interiors & Exteriors Demo Digging And Much More Marcellllo Vantosa Owner our city state and zip

Font styles to use
Serif
Sans Serif
Decorative

Colors
0054AA
0677BA
7BADD7
CADEEF
E8F1F8
0094D4
00A9DD
6FCCEA
C7EBF8
E9F6FB

Requirements
Must have
• License# 4837215
Nice to have
• Trying to go with a blue and white color scheme
Should not have
• Building construction

```html
<!DOCTYPE html>
<html lang="en">
<head>
<meta charset="utf-8">
<title>RK Teardown Business Cards</title>
<link href="https://fonts.googleapis.com/css2?family=Lato:wght@400;700;900&display=swap" rel="stylesheet">
<style>
  :root {
    --backdrop: #2c3036;
    --card: #ffffff;
    --ink: #111418;
    --muted: #6b6f75;
    --brand-blue: #1c4aa0;
    --rule-black: #111111;
  }
  * { margin: 0; padding: 0; box-sizing: border-box; }
  html, body {
    width: 1200px; height: 952px; overflow: hidden;
    background: var(--backdrop);
    font-family: "Lato", sans-serif;
  }
  .canvas { position: relative; width: 1200px; height: 952px; }
  .card {
    position: absolute; left: 220px;
    width: 760px; height: 434px;
    background: var(--card);
    box-shadow: 0 10px 28px rgba(0,0,0,.45);
    overflow: hidden;
  }
  .card--front { top: 30px; }
  .card--back { top: 488px; }

  .card__rule { position: absolute; left: 0; top: 370px; width: 760px; height: 14px; }

  /* front */
  .brand { position: absolute; left: 48px; top: 96px; }
  .brand__row { display: flex; align-items: center; gap: 12px; }
  .brand__mark { width: 22px; height: 22px; background: var(--brand-blue); }
  .brand__name { font-weight: 900; font-size: 34px; color: var(--brand-blue); letter-spacing: .5px; }
  .brand__license {
    font-size: 12px; font-weight: 700; color: var(--ink); letter-spacing: 1.5px;
    margin: 4px 0 0 34px; text-transform: uppercase;
  }

  .person { position: absolute; left: 360px; top: 80px; }
  .person__name {
    font-size: 30px; letter-spacing: 1.5px; color: var(--ink); text-transform: uppercase; font-weight: 400;
  }
  .person__name strong { font-weight: 900; color: var(--brand-blue); }
  .person__title { font-size: 15px; color: var(--muted); margin-top: 6px; margin-left: 2px; }
  .person__divider { width: 50px; height: 2px; background: var(--brand-blue); margin: 6px 0 6px 2px; }
  .person__license { font-size: 15px; font-weight: 900; color: var(--ink); }
  .person__license span { color: var(--brand-blue); }
  .person__assurance {
    font-size: 14px; font-weight: 700; color: var(--brand-blue); margin-top: 4px; letter-spacing: .3px;
  }
  .contact { list-style: none; margin-top: 14px; }
  .contact__item {
    display: flex; align-items: center; gap: 10px;
    font-size: 16px; color: var(--muted); margin-bottom: 9px;
  }
  .contact__icon {
    width: 20px; height: 20px; background: var(--brand-blue); border-radius: 3px;
    display: flex; align-items: center; justify-content: center; flex: none;
  }

  /* back */
  .identity { position: absolute; left: 40px; top: 92px; text-align: right; width: 270px; }
  .identity__name { font-weight: 900; font-size: 32px; color: var(--brand-blue); }
  .identity__tagline { font-size: 15px; color: var(--ink); line-height: 1.35; margin-top: 4px; }
  .services { position: absolute; left: 370px; top: 92px; list-style: none; }
  .services__item { font-size: 19px; color: var(--ink); line-height: 1.38; }
  .services__item::before { content: "\2022"; color: var(--brand-blue); margin-right: 6px; }
</style>
</head>
<body>
<main class="canvas">

  <section class="card card--front" aria-label="Business card front">
    <div class="brand">
      <div class="brand__row">
        <div class="brand__mark"></div>
        <div class="brand__name">RK Teardown</div>
      </div>
      <p class="brand__license">License#4837215</p>
    </div>

    <div class="person">
      <h1 class="person__name">Marcello <strong>Vantosa</strong></h1>
      <p class="person__title">Owner</p>
      <div class="person__divider"></div>
      <p class="person__license">License <span># 4837215</span></p>
      <p class="person__assurance">Licensed, Bonded, &amp; Insured</p>
      <ul class="contact">
        <li class="contact__item">
          <span class="contact__icon">
            <svg width="12" height="12" viewBox="0 0 24 24"><path fill="#fff" d="M6.6 10.8a15.1 15.1 0 0 0 6.6 6.6l2.2-2.2c.3-.3.7-.4 1-.2 1.1.4 2.3.6 3.6.6.6 0 1 .4 1 1V20c0 .6-.4 1-1 1A17 17 0 0 1 3 4c0-.6.4-1 1-1h3.5c.6 0 1 .4 1 1 0 1.3.2 2.5.6 3.6.1.3 0 .7-.2 1z"/></svg>
          </span>
          (555)318-2704
        </li>
        <li class="contact__item">
          <span class="contact__icon">
            <svg width="12" height="12" viewBox="0 0 24 24"><rect x="2" y="5" width="20" height="14" rx="1" fill="none" stroke="#fff" stroke-width="2"/><path d="M2 6l10 7 10-7" fill="none" stroke="#fff" stroke-width="2"/></svg>
          </span>
          Marcellov@brightlanecrews.com
        </li>
        <li class="contact__item">
          <span class="contact__icon">
            <svg width="12" height="12" viewBox="0 0 24 24"><path fill="#fff" d="M12 2a7 7 0 0 0-7 7c0 5 7 13 7 13s7-8 7-13a7 7 0 0 0-7-7zm0 9.5A2.5 2.5 0 1 1 12 6.5a2.5 2.5 0 0 1 0 5z"/></svg>
          </span>
          Cedar Ridge, CA, 92511
        </li>
      </ul>
    </div>

    <svg class="card__rule" viewBox="0 0 760 14" aria-hidden="true">
      <rect x="0" y="5" width="300" height="3" fill="var(--rule-black)"/>
      <polygon points="300,2 760,2 760,11 306,11" fill="var(--brand-blue)"/>
    </svg>
  </section>

  <section class="card card--back" aria-label="Business card back">
    <div class="identity">
      <h2 class="identity__name">RK Teardown</h2>
      <p class="identity__tagline">Selective Demolition<br>&amp; Full Demolition</p>
    </div>

    <ul class="services">
      <li class="services__item">Kitchens</li>
      <li class="services__item">Bathrooms</li>
      <li class="services__item">ADU Preparation</li>
      <li class="services__item">Sheds</li>
      <li class="services__item">Digging</li>
      <li class="services__item">Interiors &amp; Exteriors Demo</li>
      <li class="services__item">Much More</li>
    </ul>

    <svg class="card__rule" viewBox="0 0 760 14" aria-hidden="true">
      <rect x="0" y="5" width="300" height="3" fill="var(--rule-black)"/>
      <polygon points="300,2 760,2 760,11 306,11" fill="var(--brand-blue)"/>
    </svg>
  </section>

</main>
</body>
</html>
```